Fernvale Accounting - New Postcard for B2B marketing

I need a postcard for my business that provides cloud-based bookkeeping services with LedgerCloud Online. Our clients are small independently owned businesses. Please use our website for inspiration (colors, content, etc)... www.FernvaleAccounting.com.

Target Market(s)

Small, independently-owned businesses, including restaurants, retail stores, small medical practices, etc

Industry/Entity Type

Bookkeeper

Font styles to use
Serif

Colors
3276b5
155ea9
c4d6e9
85cae6
33a6d7

Requirements
Must have
• Must have my logo (see attached), business contact info (see website), description of services, blue color scheme
Nice to have
• Maybe add "Prices starting at $750/mo"
Content should match info on our website
4 x 6 horizontal postcard (see attached template)

```html
<!DOCTYPE html>
<html lang="en">
<head>
<meta charset="utf-8">
<title>Fernvale Accounting Postcard</title>
<link rel="stylesheet" href="https://fonts.googleapis.com/css2?family=Tinos:wght@400;700&family=PT+Sans:wght@400;700&display=swap">
<style>
  :root{
    --navy:#0d2a5c;
    --navy-deep:#0a1f47;
    --blue:#155ea9;
    --blue-mid:#3276b5;
    --teal:#33a6d7;
    --sky:#85cae6;
    --ice:#c4d6e9;
    --ink:#3b3f45;
    --paper:#ffffff;
    --mist:#f2f3f5;
    --ground:#e6e9ee;
    --serif:"Tinos", "Times New Roman", serif;
    --sans:"PT Sans", Arial, sans-serif;
  }
  *{box-sizing:border-box;margin:0;padding:0}
  html,body{width:1200px;height:800px;overflow:hidden}
  body{background:var(--ground);position:relative;font-family:var(--sans);color:var(--ink)}

  .card{position:absolute;width:570px;height:380px;background:var(--paper);overflow:hidden;box-shadow:0 4px 14px rgba(0,0,0,.18)}
  .card-front{left:30px;top:20px}
  .card-back{left:600px;top:405px}

  .layer{position:absolute;left:0;top:0}

  /* ---------- front ---------- */
  .brand{position:absolute;display:flex;align-items:center;gap:7px;font-family:var(--serif);color:var(--navy);white-space:nowrap}
  .brand-mark{width:14px;height:14px;background:var(--blue)}
  .front-brand{right:14px;top:42px;font-size:23px}
  .headline{position:absolute;right:14px;top:98px;text-align:right;font-family:var(--serif);color:var(--teal);font-size:25px;line-height:27px;letter-spacing:.3px}
  .subhead{position:absolute;right:10px;top:155px;text-align:right;font-size:12.2px;line-height:16px;color:#555a61}

  .price-badge{position:absolute;left:205px;top:132px;width:96px;height:96px;border-radius:50%;background:var(--teal);border:3px solid #fff;color:#fff;text-align:center;font-size:11.5px;line-height:15px;padding-top:14px}
  .price-badge strong{display:block;font-size:15px;margin-top:2px}

  .services{position:absolute;left:0;top:240px;width:570px;display:flex;padding:0 10px}
  .service{flex:1;padding:0 9px;border-left:1px solid rgba(255,255,255,.25)}
  .service:first-child{border-left:none}
  .service-head{display:flex;align-items:center;gap:5px;height:36px;margin-bottom:3px}
  .service-head svg{flex:none}
  .service-title{font-size:8.5px;font-weight:700;color:var(--sky);letter-spacing:.2px}
  .service p{font-size:7.6px;line-height:9px;color:#fff;text-align:justify}

  .front-footer{position:absolute;left:0;bottom:0;width:570px;height:38px}
  .phone-tab{position:absolute;left:0;top:0;height:38px;display:flex;align-items:center;gap:7px;padding-left:24px;color:#fff;font-weight:700;font-size:20px}
  .contact-strip{position:absolute;right:16px;top:11px;display:flex;gap:14px;font-size:11px;color:var(--navy);align-items:center}
  .contact-strip span{display:flex;align-items:center;gap:4px}

  /* ---------- back ---------- */
  .back-brand{left:47px;top:50px;font-size:23px}
  .vision-tab{position:absolute;left:0;top:96px;height:24px;width:140px;background:var(--teal);clip-path:polygon(0 0,100% 0,88% 100%,0 100%);color:#fff;font-family:var(--serif);font-size:15px;line-height:24px;padding-left:12px;letter-spacing:.3px}
  .vision-copy{position:absolute;left:12px;top:128px;width:215px;font-size:9.8px;line-height:12.6px;color:#3f434a}
  .vision-copy.founded{top:203px;width:290px}

  .screen-ring{position:absolute;left:225px;top:60px;width:130px;height:130px;border-radius:50%;border:5px solid var(--teal);background:#fff;padding:3px}
  .screen-fill{width:100%;height:100%;border-radius:50%;background:linear-gradient(135deg,#eef2f7 0%,#d8e2ee 55%,#9fb2c8 100%)}

  .cert-row{position:absolute;left:12px;top:256px;display:flex;align-items:center;gap:14px}
  .cert-badge{width:36px;height:46px;background:#fff;border-bottom:6px solid #6cbf4a}
  .cert-text{color:#fff;font-size:8.6px;line-height:11px;width:220px}
  .contact-bar{position:absolute;left:0;top:312px;height:32px;display:flex;align-items:center;gap:8px;padding-left:30px;color:#fff;font-size:18px}
  .contact-bar b{font-weight:700;font-size:17px}
  .back-url{position:absolute;left:45px;top:348px;color:#fff;font-size:19px}

  .stamp-box{position:absolute;left:457px;top:25px;width:97px;height:65px;border:1px solid #b9bec6}
  .address-line{position:absolute;height:1px;background:#b9bec6}
</style>
</head>
<body>

<!-- Front of postcard -->
<section class="card card-front" aria-label="Postcard front">
  <svg class="layer" width="570" height="380" viewBox="0 0 570 380" aria-hidden="true">
    <defs>
      <linearGradient id="navyPanel" x1="0" y1="0" x2="1" y2="1">
        <stop offset="0" stop-color="#1a4c8e"/>
        <stop offset="1" stop-color="#0a1f47"/>
      </linearGradient>
    </defs>
    <rect x="0" y="0" width="570" height="12" fill="#0d2a5c"/>
    <polygon points="320,0 330,0 330,12 320,12" fill="#0d2a5c"/>
    <polygon points="0,210 570,210 570,380 0,380" fill="url(#navyPanel)"/>
    <polygon points="326,12 340,12 262,210 248,210" fill="#c4d6e9"/>
  </svg>

  <div class="layer" role="img" aria-label="Photo of four business colleagues reviewing documents at a desk"
       style="width:330px;height:210px;top:12px;background:linear-gradient(120deg,#d9dde3 0%,#a9b3c0 45%,#5a6a80 100%);clip-path:polygon(0 0,100% 0,76% 94%,0 94%)"></div>

  <div class="brand front-brand"><span class="brand-mark"></span>Fernvale Accounting</div>
  <h1 class="headline">BOUTIQUE<br>ACCOUNTING FIRM</h1>
  <p class="subhead">Specializing in Small Business Bookkeeping<br>&amp; Payroll Processing with LedgerCloud<br>Online</p>

  <div class="price-badge">Full Service<br>Bookkeeping<br>starting at<strong>$750/mo</strong></div>

  <div class="services">
    <div class="service">
      <div class="service-head">
        <svg width="30" height="30" viewBox="0 0 30 30" aria-hidden="true">
          <circle cx="15" cy="15" r="13" fill="#33a6d7"/>
          <text x="15" y="20.5" text-anchor="middle" font-size="16" font-weight="700" fill="#fff" font-family="PT Sans, Arial, sans-serif">$</text>
        </svg>
        <span class="service-title">BOOKKEEPING</span>
      </div>
      <p>Let us take over the day to day bookkeeping so you can get back to running your business. We offer LedgerCloud Online setup and ongoing bookkeeping, including daily journal entries, accounts payables &amp; receivables, bill pay, sales tax reporting &amp; payments, account reconciliation, and more.</p>
    </div>
    <div class="service">
      <div class="service-head">
        <svg width="30" height="30" viewBox="0 0 30 30" aria-hidden="true" fill="none" stroke="#fff" stroke-width="1.4">
          <rect x="5" y="3" width="20" height="24" rx="1"/>
          <rect x="9" y="13" width="3" height="8" fill="#33a6d7" stroke="none"/>
          <rect x="14" y="9" width="3" height="12" fill="#33a6d7" stroke="none"/>
          <rect x="19" y="15" width="3" height="6" fill="#33a6d7" stroke="none"/>
          <line x1="8" y1="24" x2="22" y2="24"/>
        </svg>
        <span class="service-title">FINANCIAL REPORTING</span>
      </div>
      <p>We'll provide easy to understand financial reports that allow you and your team to manage cash flow, create budgets and make forecasting decisions. Want real time data? Let us provide solutions with the latest in mobile apps and dashboards.</p>
    </div>
    <div class="service">
      <div class="service-head">
        <svg width="30" height="30" viewBox="0 0 30 30" aria-hidden="true" fill="none" stroke="#fff" stroke-width="1.4">
          <circle cx="15" cy="7" r="3.5" fill="#33a6d7" stroke="none"/>
          <circle cx="7" cy="11" r="3"/>
          <circle cx="23" cy="11" r="3"/>
          <path d="M2 26v-6a5 5 0 0 1 10 0M18 20a5 5 0 0 1 10 0v6"/>
          <rect x="10" y="17" width="10" height="8" rx="1"/>
        </svg>
        <span class="service-title">PAYROLL PROCESSING</span>
      </div>
      <p>Whether you have 5 employees or 100+, payroll can be an overwhelming and time consuming task. We offer full service payroll processing, including employee on boarding and reporting.</p>
    </div>
  </div>

  <div class="front-footer">
    <svg class="layer" width="570" height="38" viewBox="0 0 570 38" aria-hidden="true">
      <rect width="570" height="38" fill="#0d2a5c"/>
      <polygon points="192,3 570,3 570,32 202,32" fill="#fff"/>
      <polygon points="0,0 192,0 204,38 0,38" fill="#33a6d7"/>
    </svg>
    <div class="phone-tab">
      <svg width="14" height="14" viewBox="0 0 24 24" aria-hidden="true"><circle cx="12" cy="12" r="10.5" fill="none" stroke="#fff" stroke-width="2"/><path d="M8 6.5l2 0 1 3-1.5 1.2a7 7 0 0 0 3.8 3.8L14.5 13l3 1v2a1.5 1.5 0 0 1-1.6 1.5A10 10 0 0 1 6.5 8.1 1.5 1.5 0 0 1 8 6.5z" fill="#fff"/></svg>
      1.800.555.0142
    </div>
    <div class="contact-strip">
      <span><svg width="10" height="8" viewBox="0 0 10 8" aria-hidden="true"><rect x=".5" y=".5" width="9" height="7" fill="none" stroke="#0d2a5c"/><path d="M.5.5L5 4.5 9.5.5" fill="none" stroke="#0d2a5c"/></svg>info@fernvaleaccounting.com</span>
      <span><svg width="9" height="9" viewBox="0 0 10 10" aria-hidden="true"><circle cx="5" cy="5" r="4.3" fill="none" stroke="#0d2a5c"/><ellipse cx="5" cy="5" rx="2" ry="4.3" fill="none" stroke="#0d2a5c"/><line x1=".7" y1="5" x2="9.3" y2="5" stroke="#0d2a5c"/></svg>www.fernvaleaccounting.com</span>
    </div>
  </div>
</section>

<!-- Back of postcard -->
<section class="card card-back" aria-label="Postcard back">
  <svg class="layer" width="570" height="380" viewBox="0 0 570 380" aria-hidden="true">
    <defs>
      <linearGradient id="navyBand" x1="0" y1="0" x2="1" y2="1">
        <stop offset="0" stop-color="#1a4c8e"/>
        <stop offset="1" stop-color="#0a1f47"/>
      </linearGradient>
    </defs>
    <polygon points="0,0 268,0 352,380 0,380" fill="#f2f3f5"/>
    <polygon points="0,243 322,243 352,380 0,380" fill="url(#navyBand)"/>
    <polygon points="0,312 318,312 326,344 0,344" fill="#33a6d7"/>
  </svg>

  <div class="brand back-brand"><span class="brand-mark"></span>Fernvale Accounting</div>
  <div class="vision-tab">OUR VISION</div>
  <p class="vision-copy">At Fernvale Accounting we have one mission in mind... to improve the quality, accuracy and efficiency of your business's back-end bookkeeping and payroll processing, so that you can focus on the nuts and bolts of your day to day operations.</p>
  <p class="vision-copy founded">Founded by a former CFO in the San Francisco Bay Area, we bring a team of accounting professionals with over 20 years of expertise from one of the most competitive markets in the world.</p>

  <div class="screen-ring"><div class="screen-fill" role="img" aria-label="Laptop showing an online bookkeeping dashboard"></div></div>

  <div class="cert-row">
    <div class="cert-badge"></div>
    <p class="cert-text">Our Certified LedgerCloud Advisors have the Knowledge and Expertise to Ensure Professional, Accurate, High Quality Service.</p>
  </div>
  <div class="contact-bar">CONTACT US
    <svg width="14" height="14" viewBox="0 0 24 24" aria-hidden="true"><circle cx="12" cy="12" r="10.5" fill="none" stroke="#fff" stroke-width="2"/><path d="M8 6.5l2 0 1 3-1.5 1.2a7 7 0 0 0 3.8 3.8L14.5 13l3 1v2a1.5 1.5 0 0 1-1.6 1.5A10 10 0 0 1 6.5 8.1 1.5 1.5 0 0 1 8 6.5z" fill="#fff"/></svg>
    <b>1.800.555.0142</b></div>
  <div class="back-url">www.fernvaleaccounting.com</div>

  <div class="stamp-box"></div>
  <div class="address-line" style="left:365px;top:150px;width:190px"></div>
  <div class="address-line" style="left:335px;top:196px;width:220px"></div>
  <div class="address-line" style="left:365px;top:238px;width:190px"></div>
</section>

</body>
</html>
```